Business Card Design & Logo Design

Im a new company selling: balloons, bespoke gift wrapping services & Christmas decorating services i.e. I will come and decorate your tree, wrap your xmas presents, set & decorate your dining table, help you host your xmas party etc. etc.

I don't do 'cheesey' stuff so need a sophisticated card.

I love b&w colours, I love stripes and smart looking stuff.

I do already have an idea and if I don't find anything else then I will go with my idea but would then just need somebody to create the artwork for me.

www.copperwillow.co.uk is currently in the process of being designed so any ideas of logos/designs must also work with a website.

Industry/Entity Type

Business

Contact Information for Business Card

Copper Willow
Ashcombe Vale
KT14 9RD
Westbrookshire
01632 960418
or
07700 900736

treats@copperwillow.co.uk

```html
<!DOCTYPE html>
<html lang="en">
<head>
<meta charset="utf-8">
<title>Copper Willow – Business Card</title>
<link rel="stylesheet" href="https://fonts.googleapis.com/css2?family=Arimo:wght@700&display=swap">
<style>
  :root {
    --page-bg: #ececec;
    --card-black: #0b0b0b;
    --card-stripe: #2b2b2b;
    --ink-white: #ffffff;
    --brand-silver: #d9d9d9;
    --card-shadow: rgba(0, 0, 0, 0.28);
  }
  * { box-sizing: border-box; margin: 0; padding: 0; }
  html, body {
    width: 1200px;
    height: 900px;
    overflow: hidden;
    background: var(--page-bg);
  }
  .canvas {
    position: relative;
    width: 1200px;
    height: 900px;
  }
  .business-card {
    position: absolute;
    left: 120px;
    top: 140px;
    width: 960px;
    height: 620px;
    border-radius: 40px;
    overflow: hidden;
    background: repeating-linear-gradient(
      to bottom,
      var(--card-black) 0,
      var(--card-black) 20px,
      var(--card-stripe) 20px,
      var(--card-stripe) 39px
    );
    box-shadow: 0 18px 40px var(--card-shadow);
  }
  .brand-name {
    position: absolute;
    top: 178px;
    left: 0;
    width: 100%;
    text-align: center;
    font-family: "Arimo", Arial, sans-serif;
    font-weight: 700;
    font-size: 76px;
    letter-spacing: 4px;
    text-transform: uppercase;
    color: var(--brand-silver);
  }
  .contact-list {
    position: absolute;
    left: 52px;
    top: 384px;
    list-style: none;
    font-family: "Arimo", Arial, sans-serif;
    font-weight: 700;
    font-size: 29px;
    line-height: 40px;
    color: var(--ink-white);
  }
  .contact-item {
    display: flex;
    align-items: center;
    gap: 10px;
  }
  .contact-icon {
    width: 28px;
    height: 28px;
    flex: none;
    fill: var(--ink-white);
  }
</style>
</head>
<body>
<main class="canvas">
  <section class="business-card" aria-label="Copper Willow business card">
    <h1 class="brand-name">Copper Willow</h1>

    <ul class="contact-list">
      <li class="contact-item">
        <svg class="contact-icon" viewBox="0 0 24 24" aria-hidden="true">
          <path d="M6.6 10.8a15.1 15.1 0 0 0 6.6 6.6l2.2-2.2a1 1 0 0 1 1-.25 11.4 11.4 0 0 0 3.6.57 1 1 0 0 1 1 1V20a1 1 0 0 1-1 1A17 17 0 0 1 3 4a1 1 0 0 1 1-1h3.5a1 1 0 0 1 1 1c0 1.25.2 2.45.57 3.57a1 1 0 0 1-.25 1z"/>
        </svg>
        <span>01632 960418</span>
      </li>
      <li class="contact-item">
        <svg class="contact-icon" viewBox="0 0 24 24" aria-hidden="true">
          <path d="M6.6 10.8a15.1 15.1 0 0 0 6.6 6.6l2.2-2.2a1 1 0 0 1 1-.25 11.4 11.4 0 0 0 3.6.57 1 1 0 0 1 1 1V20a1 1 0 0 1-1 1A17 17 0 0 1 3 4a1 1 0 0 1 1-1h3.5a1 1 0 0 1 1 1c0 1.25.2 2.45.57 3.57a1 1 0 0 1-.25 1z"/>
        </svg>
        <span>07700 900736</span>
      </li>
      <li class="contact-item">
        <svg class="contact-icon" viewBox="0 0 24 24" aria-hidden="true">
          <path d="M2 6a2 2 0 0 1 2-2h16a2 2 0 0 1 2 2v12a2 2 0 0 1-2 2H4a2 2 0 0 1-2-2zm2.4 0L12 11.6 19.6 6zM4 8v10h16V8l-8 5.8z"/>
        </svg>
        <span>treats@copperwillow.co.uk</span>
      </li>
      <li class="contact-item">
        <svg class="contact-icon" viewBox="0 0 24 24" aria-hidden="true">
          <path d="M12 3 1.5 12h3v9h6v-6h3v6h6v-9h3z"/>
        </svg>
        <span>Ashcombe Vale KT14 9RD Westbrookshire</span>
      </li>
    </ul>
  </section>
</main>
</body>
</html>
```